Healthy Lifestyle Vitamin Supplement Company needs a web site designed.

We are starting a new website for selling quality natural vitamins and supplements online plus providing news and information on healthy living. We DO NOT need any programming done for this site. Just the design in a layered photoshop file. This site needs to communicate that we are the authoritative source for healthy living and a trusted place to buy supplements and information on living a healthy lifestyle.

Triggers On page will be

Trigger set 1
Home - Shop By Brand - Top Sellers - Clearance - Help Center - My Favorites

Trigger set 2
Vitamins and Herbs - Natural Living - Aromatherapy - Coffee and Tea - Health and Beauty - Healthy Foods - Pet Health - Sports and Diet

Triggers Other
Login - Shopping Cart - Checkout - Track Order

Need a search bar in the design

Left side should be categories look at Brelvox.com for example of categories.

Name and domain name is Sunward Meadow Crest

Will also need a logo to go along with that.

Industry/Entity Type

It Company

```html
<!DOCTYPE html>
<html lang="en">
<head>
<meta charset="utf-8">
<title>Sunward Meadow Crest — Quality Natural Vitamins &amp; Supplements</title>
<link rel="stylesheet" href="https://fonts.googleapis.com/css2?family=Raleway:wght@400;500;600;800&family=Open+Sans:wght@400;600&display=swap">
<style>
:root{
  --navy:#0f5d9b;
  --navy-dark:#0b4f86;
  --sky:#1aa6ec;
  --sky-dark:#1296db;
  --title:#1a67ab;
  --heading:#16487a;
  --orange:#f27b1f;
  --text:#555d66;
  --muted:#8a9098;
  --line:#dde1e5;
  --band:#f3f4f6;
  --white:#ffffff;
}
*{box-sizing:border-box;margin:0;padding:0}
html,body{width:986px;height:1200px;overflow:hidden;background:var(--white)}
body{position:relative;font-family:"Open Sans",Arial,sans-serif;color:var(--text)}
.abs{position:absolute}

/* header */
.hero-band{left:0;top:114px;width:986px;height:350px;background:linear-gradient(#eef0f2,#f7f8f9 30%,#ffffff 55%,#f7f8f9 85%,#eef0f2);border-bottom:1px solid #e2e5e8}
.header-rule{left:0;top:114px;width:986px;height:1px;background:#e2e5e8}
.toplinks{right:126px;top:5px;font-size:10px;color:#444}
.toplinks span{margin:0 5px}
.brand{left:122px;top:28px;font-family:"Raleway",sans-serif;font-weight:500;font-size:24px;color:var(--title);letter-spacing:-.2px}
.slogan{left:123px;top:58px;font-size:10px;color:#7ab3dc}
.search{left:436px;top:46px;width:212px;height:22px;border:1px solid #cfd4d8;border-radius:2px;background:#fff;font-size:8px;line-height:20px;padding-left:8px;color:#555}
.search-btn{left:626px;top:44px;width:26px;height:26px;border-radius:50%;background:var(--sky)}
.support{right:126px;top:40px;text-align:right;font-family:"Raleway",sans-serif}
.support .label{font-size:12px;color:var(--orange)}
.support .phone{font-size:18px;color:var(--heading);font-weight:500;display:flex;align-items:center;gap:2px}

.nav-main{left:122px;top:83px;width:744px;height:34px;background:linear-gradient(var(--navy),var(--navy-dark));display:flex;font-family:"Raleway",sans-serif;font-size:11.5px;color:#fff;font-weight:500}
.nav-main a{display:block;line-height:34px;padding:0 16px;border-right:1px solid #0a4675;color:#fff;text-decoration:none}
.nav-main a:first-child{padding:0 16px 0 27px}
.nav-main a:last-child{border-right:0}
.nav-sub{left:122px;top:117px;width:744px;height:25px;background:linear-gradient(var(--sky),var(--sky-dark));display:flex;font-family:"Raleway",sans-serif;font-size:10px;color:#fff}
.nav-sub a{display:block;line-height:25px;padding:0 9px;border-right:1px solid #5cc3f3;color:#fff;text-decoration:none}
.nav-sub a:first-child{padding-left:24px}
.nav-sub a:last-child{border-right:0}

/* hero */
.hero-title{left:130px;top:218px;font-family:"Raleway",sans-serif;font-weight:800;font-size:32.5px;color:var(--orange);letter-spacing:.3px}
.hero-sub{left:131px;top:256px;font-family:"Raleway",sans-serif;font-weight:600;font-size:21px;color:var(--heading);letter-spacing:.3px}
.hero-text{left:132px;top:285px;width:270px;font-size:9px;line-height:13px;color:#666}
.dots{left:133px;top:319px;display:flex;gap:3px}
.dots i{width:10px;height:10px;border-radius:50%;background:#c9cdd1;display:block}
.dots i:first-child{background:var(--sky)}
.hero-art{left:530px;top:176px;width:280px;height:208px}

/* feature boxes */
.features{left:122px;top:422px;width:742px;height:121px;background:#fff;border:1px solid var(--line);display:flex;box-shadow:0 1px 2px rgba(0,0,0,.04)}
.feature{position:relative;flex:1;border-right:1px solid var(--line);padding:16px 0 0 18px}
.feature:last-child{border-right:0}
.feature h3{position:relative;z-index:1;font-family:"Raleway",sans-serif;font-weight:500;font-size:15.5px;color:var(--sky-dark);white-space:nowrap}
.feature p{position:relative;z-index:1;margin-top:4px;width:148px;font-size:8px;line-height:12.8px;color:#888}
.feature .more{margin-top:5px;font-family:"Raleway",sans-serif;font-weight:600;font-size:9.5px;color:var(--title)}
.feature .pic{position:absolute;top:20px}

/* sidebar */
.sidebar{left:122px;top:564px;width:167px;height:379px;border:1px solid var(--line);background:#fff}
.sidebar-head{height:32px;background:linear-gradient(#f68a2c,#ef7415);color:#fff;font-family:"Raleway",sans-serif;font-size:14px;line-height:32px;padding-left:19px}
.cats{list-style:none;margin:8px 0 0 20px;width:133px}
.cats li{height:17.1px;border-bottom:1px solid #eceef0;font-size:8px;line-height:17px;color:#666;padding-left:16px;position:relative}
.cats li::before{content:"";position:absolute;left:4px;top:6px;width:3px;height:3px;border-right:1px solid #aaa;border-top:1px solid #aaa;transform:rotate(45deg)}
.cats li .tag{margin-left:16px}

/* products */
.grid{left:301px;width:564px;height:182px;display:flex;border:1px solid var(--line);background:#fff}
.product{flex:1;border-right:1px solid var(--line);position:relative;text-align:center}
.product:last-child{border-right:0}
.product .pic{position:absolute;left:50%;transform:translateX(-50%);top:24px}
.product .name{position:absolute;left:0;right:0;top:119px;font-family:"Raleway",sans-serif;font-size:12.5px;color:var(--title);font-weight:500}
.product .desc{position:absolute;left:0;right:0;top:136px;font-size:7.8px;color:#999}
.product .price{position:absolute;left:14px;top:153px;font-family:"Raleway",sans-serif;font-size:13.5px;color:var(--heading)}
.product .cart{position:absolute;left:65px;top:153px;width:67px;height:18px;background:var(--sky);color:#fff;font-size:8px;font-weight:600;line-height:18px;border-radius:1px}

/* footer */
.footer-rule{left:0;top:982px;width:986px;height:1px;background:#dfe2e5}
.footer-band{left:0;top:983px;width:986px;height:173px;background:linear-gradient(#fff,#f5f6f7)}
.fcol{top:1010px}
.fcol h4{font-family:"Raleway",sans-serif;font-weight:500;font-size:13.5px;color:var(--heading);margin-bottom:4px}
.fcol li{list-style:none;font-size:9px;line-height:17.7px;color:#666}
.social{display:flex;gap:7px;margin-top:5px}
.social span{font-family:"Raleway",sans-serif;font-weight:600;font-size:9px;color:var(--title)}
.pay-label{font-size:9px;color:var(--heading);margin-top:9px}
.cards{display:flex;gap:6px;margin-top:5px}
.cards span{width:24px;height:15px;border:1px solid #aab;font-size:5.5px;line-height:13px;text-align:center;color:#334;background:#fff}
.bottom-rule{left:0;top:1156px;width:986px;height:1px;background:#dfe2e5}
.copyright{left:122px;top:1173px;font-size:8px;color:#666}
</style>
</head>
<body>

<div class="abs hero-band"></div>
<div class="abs header-rule"></div>

<div class="abs toplinks">Login<span>|</span>Shopping Cart<span>|</span>Checkout<span>|</span>Track Order</div>
<div class="abs brand">Sunward Meadow Crest</div>
<div class="abs slogan">Your Slogan goes here</div>
<div class="abs search">Product Search</div>
<div class="abs search-btn">
  <svg width="26" height="26" viewBox="0 0 26 26"><circle cx="12" cy="12" r="5" fill="none" stroke="#fff" stroke-width="2"/><line x1="15.5" y1="15.5" x2="19" y2="19" stroke="#fff" stroke-width="2.2" stroke-linecap="round"/></svg>
</div>
<div class="abs support">
  <div class="label">Customer Support</div>
  <div class="phone">
    <svg width="15" height="15" viewBox="0 0 24 24"><path d="M6.6 10.8c1.4 2.8 3.8 5.1 6.6 6.6l2.2-2.2c.3-.3.7-.4 1-.2 1.1.4 2.3.6 3.6.6.6 0 1 .4 1 1V20c0 .6-.4 1-1 1C10.6 21 3 13.4 3 4c0-.6.4-1 1-1h3.5c.6 0 1 .4 1 1 0 1.3.2 2.5.6 3.6.1.3 0 .7-.2 1L6.6 10.8z" fill="#f27b1f"/></svg>
    1800.555.0142
  </div>
</div>

<nav class="abs nav-main">
  <a>Home</a><a>Shop By Brand</a><a>Top Sellers</a><a>Clearance</a><a>Help Center</a><a>My Favorites</a>
</nav>
<nav class="abs nav-sub">
  <a>Vitamins and Herbs</a><a>Natural Living</a><a>Aromatherapy</a><a>Coffee and Tea</a><a>Health and Beauty</a><a>Healthy Foods</a><a>Pet Health</a><a>Sports and Diet</a>
</nav>

<div class="abs hero-title">QUALITY NATURAL</div>
<div class="abs hero-sub">VITAMINS &amp; SUPPLEMENTS</div>
<div class="abs hero-text">Etiam est nunc venenatis in tristique eu imperdiet ac nisl Cum sociis natoque penatibus et magnis dis parturien</div>
<div class="abs dots"><i></i><i></i><i></i><i></i></div>
<div class="abs hero-art" role="img" aria-label="Three large dark tubs of whey protein powder">
  <svg width="280" height="208" viewBox="0 0 280 208">
    <defs><linearGradient id="tub" x1="0" x2="1"><stop offset="0" stop-color="#1c1d1f"/><stop offset=".5" stop-color="#4a4c50"/><stop offset="1" stop-color="#1c1d1f"/></linearGradient></defs>
    <rect x="6" y="28" width="100" height="170" rx="22" fill="url(#tub)"/>
    <rect x="174" y="28" width="100" height="170" rx="22" fill="url(#tub)"/>
    <rect x="82" y="8" width="124" height="196" rx="24" fill="url(#tub)"/>
  </svg>
</div>

<section class="abs features">
  <div class="feature">
    <h3>Why Our Product</h3>
    <p>Etiam est nunc venenatis in tristique eu imperdiet ac nisl Cum sociis natoque penatibus et magnis dis parturient montes nascetu</p>
    <div class="more">Shop Now ▸</div>
    <div class="pic" style="left:180px;width:46px;height:86px;border-radius:6px;background:linear-gradient(#3a2f6e,#6f64a8 45%,#d8d6e6)" role="img" aria-label="Tub of lean protein powder"></div>
  </div>
  <div class="feature">
    <h3>Quality Vitmanis</h3>
    <p>Etiam est nunc venenatis in tristique eu imperdiet ac nisl Cum sociis natoque penatibus et magnis dis parturient montes nascetu</p>
    <div class="more">Shop Now ▸</div>
    <div class="pic" style="left:172px;width:54px;height:82px;border-radius:6px;background:linear-gradient(#e9eef2,#2f9fd3 40%,#58c2e8)" role="img" aria-label="Jar of vitamin E capsules"></div>
  </div>
  <div class="feature">
    <h3>Brand Supplements</h3>
    <p>Etiam est nunc venenatis in tristique eu imperdiet ac nisl Cum sociis natoque penatibus et magnis dis parturient montes nascetu</p>
    <div class="more">Shop Now ▸</div>
    <div class="pic" style="left:172px;top:42px;width:68px;height:72px;border-radius:8px;background:linear-gradient(90deg,#5e8a4a,#f4f6f4 35%,#ffffff 65%,#c9302c)" role="img" aria-label="Supplement bottle with herbs and red berries"></div>
  </div>
</section>

<aside class="abs sidebar">
  <div class="sidebar-head">Product Category</div>
  <ul class="cats">
    <li>A &amp; D Vitamins</li><li>Acidophilus/Probiotics</li><li>Amino Acid Supplements</li><li>Antioxidants</li><li>B Vitamins</li><li>B-12 Vitamins</li><li>B-Complex Vitamins</li><li>Babies &amp; Kids<span class="tag">newtag</span></li><li>C Vitamins</li><li>Calcium Supplements</li><li>Co Q-10</li><li>D Vitamins</li><li>Diet &amp; Lifestyle</li><li>Digestive Health</li><li>E Vitamins</li><li>Eye Health</li><li>Fish Oils</li><li>Garcinia Cambogia</li><li>Health &amp; Beauty</li>
  </ul>
</aside>

<section class="abs grid" style="top:564px">
  <div class="product"><div class="pic" style="width:68px;height:74px;border-radius:6px;background:linear-gradient(#b5161c,#e12a2f 50%,#9c1015)" role="img" aria-label="Red tub of energy formula"></div><div class="name">Product Name</div><div class="desc">Etiam est nunc venenatis ded</div><div class="price">$25.99</div><div class="cart">Add to Cart</div></div>
  <div class="product"><div class="pic" style="width:82px;height:78px;border-radius:4px;background:linear-gradient(90deg,#3b4a2e,#e8efe0 50%,#8cc04b)" role="img" aria-label="Garcinia cambogia bottle and box"></div><div class="name">Product Name</div><div class="desc">Etiam est nunc venenatis ded</div><div class="price">$25.99</div><div class="cart">Add to Cart</div></div>
  <div class="product"><div class="pic" style="width:46px;height:76px;border-radius:5px;background:linear-gradient(#2a2a2e,#4a4a52 50%,#1e1e22)" role="img" aria-label="Dark tub of pre-workout powder"></div><div class="name">Product Name</div><div class="desc">Etiam est nunc venenatis ded</div><div class="price">$25.99</div><div class="cart">Add to Cart</div></div>
  <div class="product"><div class="pic" style="width:56px;height:84px;border-radius:6px;background:linear-gradient(#0e1a12,#2b4a30 50%,#0c1510)" role="img" aria-label="Black tub of creatine powder"></div><div class="name">Product Name</div><div class="desc">Etiam est nunc venenatis ded</div><div class="price">$25.99</div><div class="cart">Add to Cart</div></div>
</section>

<section class="abs grid" style="top:758px">
  <div class="product"><div class="pic" style="width:48px;height:88px;border-radius:8px;background:linear-gradient(#f4f4f2,#f3a43a 45%,#fde7c0)" role="img" aria-label="Bottle of vitamin E with selenium"></div><div class="name">Product Name</div><div class="desc">Etiam est nunc venenatis ded</div><div class="price">$25.99</div><div class="cart">Add to Cart</div></div>
  <div class="product"><div class="pic" style="width:38px;height:88px;border-radius:8px;background:linear-gradient(#3d3e1e,#7a7a3a 50%,#4a4b22)" role="img" aria-label="Olive bottle of natural vitamin E"></div><div class="name">Product Name</div><div class="desc">Etiam est nunc venenatis ded</div><div class="price">$25.99</div><div class="cart">Add to Cart</div></div>
  <div class="product"><div class="pic" style="width:48px;height:94px;border-radius:8px;background:linear-gradient(#f4f5f8,#2e3f8f 45%,#e9ebf3)" role="img" aria-label="White bottle with blue label of gamma E"></div><div class="name">Product Name</div><div class="desc">Etiam est nunc venenatis ded</div><div class="price">$25.99</div><div class="cart">Add to Cart</div></div>
  <div class="product"><div class="pic" style="width:52px;height:92px;border-radius:8px;background:linear-gradient(#f6f7f9,#e8ecf3 45%,#f0f2f6)" role="img" aria-label="White bottle of eye health supplement"></div><div class="name">Product Name</div><div class="desc">Etiam est nunc venenatis ded</div><div class="price">$25.99</div><div class="cart">Add to Cart</div></div>
</section>

<div class="abs footer-rule"></div>
<div class="abs footer-band"></div>
<div class="abs fcol" style="left:130px"><h4>Information</h4><ul><li>Shop By Brand</li><li>Top Sellers</li><li>Clearance</li><li>Help Center</li><li>My Favorites</li></ul></div>
<div class="abs fcol" style="left:256px"><h4>Best Sellings</h4><ul><li>Morbi diam mauris</li><li>Viverra gravida</li><li>Eu mattis in ante</li><li>Morbi eget</li><li>Arcu Morbi</li></ul></div>
<div class="abs fcol" style="left:389px"><h4>Resources</h4><ul><li>Vitamins and Herbs</li><li>Natural Living</li><li>Aromatherapy</li><li>Coffee and Tea</li><li>Health and Beauty</li></ul></div>
<div class="abs fcol" style="left:522px"><h4>Support</h4><ul><li>Term of Use</li><li>FAQ</li><li>Customer Support</li><li>Contact Us</li><li>Privacy Policy</li></ul></div>
<div class="abs fcol" style="left:661px">
  <h4>Get in touch</h4>
  <ul><li>Please connect with us on.</li></ul>
  <div class="social"><span>Chirpa</span><span>Facio</span><span>Linkt</span><span>Orbix</span></div>
  <div class="pay-label">Make Payments</div>
  <div class="cards"><span>Medra</span><span>Vantis</span><span>Amtel</span><span>Dovra</span><span>ePayd</span></div>
</div>
<div class="abs bottom-rule"></div>
<div class="abs copyright">© 2014 Company Name &nbsp;All right reserved &nbsp;Term of Use</div>

</body>
</html>
```